General Dental Office Business Card

I run a private general dental office in southern California, and would like a refresh/redesign of my business card. I focus on quality care rather than volume. The email address on the uploaded current card should be updated to: info@marbleshoredental.example. The current card's logo is a deboss, but I am open to other ideas. The logo can be refreshed, but it is something that's been with me since the beginning of the office, so I wouldn't want a drastic redesign.
Target Market(s)
Adults 18-99, whoever needs dental services
Industry/Entity Type
Healthcare/Dental
Contact Information for Business Card
Name, Address, Phone, email
Colors
Designer to choose colors to be used in the design.
Requirements
Must have
- Logo (Same as original one in the uploaded file), space on back for appointment time/date

```html
<!DOCTYPE html>
<html lang="en">
<head>
<meta charset="utf-8">
<title>Marble Shore Dental — Business Card</title>
<link href="https://fonts.googleapis.com/css2?family=Varela+Round&display=swap" rel="stylesheet">
<style>
  :root {
    --bg: #2b2b2d;
    --card: #ffffff;
    --blue: #4fb8d6;
    --blue-light: #84d2ea;
    --blue-pale: #d6f0f8;
    --grey: #6b6b6b;
    --rule: #8a8a8a;
    --ghost: #f1f7fa;
  }
  * { box-sizing: border-box; margin: 0; padding: 0; }
  html, body { width: 1200px; height: 900px; overflow: hidden; }
  body {
    background: var(--bg);
    font-family: "Varela Round", "Helvetica Neue", Arial, sans-serif;
    position: relative;
  }
  .card {
    position: absolute;
    top: 100px;
    width: 400px;
    height: 700px;
    background: var(--card);
    overflow: hidden;
  }
  .card--front { left: 170px; }
  .card--back { left: 630px; }

  /* Front */
  .dentist { position: absolute; left: 34px; top: 40px; }
  .dentist__name { color: var(--blue); font-size: 28px; font-weight: 400; letter-spacing: .5px; }
  .dentist__title { color: var(--grey); font-size: 17px; margin-top: 4px; letter-spacing: .5px; }
  .brand-vertical {
    position: absolute;
    right: 14px;
    top: 26px;
    writing-mode: vertical-rl;
    color: var(--blue);
    font-size: 54px;
    line-height: 1;
    letter-spacing: 1px;
  }
  .ghost-mark {
    position: absolute;
    left: 70px; top: 250px;
    width: 200px; height: 200px;
    border: 10px solid var(--ghost);
    border-radius: 50%;
    display: flex; align-items: center; justify-content: center;
    text-align: center;
    color: var(--ghost);
    font-size: 20px;
    line-height: 1.3;
  }
  .contact { position: absolute; left: 34px; bottom: 40px; font-size: 17px; line-height: 1.55; }
  .contact__address { color: var(--blue); margin-bottom: 6px; }
  .contact__line { color: var(--grey); display: flex; align-items: center; gap: 9px; }
  .contact__line svg { width: 15px; height: 15px; flex: none; }

  /* Back */
  .appointment { position: absolute; left: 40px; right: 40px; top: 48px; }
  .appointment__field { border-top: 1px solid var(--rule); text-align: center; color: var(--grey); font-size: 15px; padding-top: 6px; margin-bottom: 46px; letter-spacing: .5px; }
  .back-mark {
    position: absolute;
    left: 90px; top: 210px;
    width: 220px; height: 220px;
    border: 12px solid var(--blue-light);
    border-radius: 50%;
    display: flex; align-items: center; justify-content: center;
    text-align: center;
    color: var(--blue-light);
    font-size: 24px;
    line-height: 1.3;
  }
  .wave-band {
    position: absolute; left: 0; right: 0; bottom: 0;
    height: 200px;
    background: linear-gradient(to bottom, var(--blue-pale) 0%, var(--blue-light) 45%, var(--blue-light) 100%);
  }
  .band-name {
    position: absolute; left: 0; right: 0; bottom: 44px;
    text-align: center; color: #fff; font-size: 34px; letter-spacing: .5px;
  }
</style>
</head>
<body>

<section class="card card--front">
  <div class="dentist">
    <h1 class="dentist__name">Elliot M. Varga DDS</h1>
    <p class="dentist__title">General Dentistry</p>
  </div>

  <div class="brand-vertical">Marble Shore Dental</div>

  <div class="ghost-mark" aria-hidden="true">Marble Shore<br>Dental</div>

  <div class="contact">
    <p class="contact__address">1820 Cove Terrace<br>Marble Shore, CA 90000</p>
    <p class="contact__line">
      <svg viewBox="0 0 16 16" fill="var(--blue)"><path d="M3 2l3 0 1 3-2 1c1 2 3 4 5 5l1-2 3 1 0 3c-7 0-11-4-11-11z"/></svg>
      555-014-2828
    </p>
    <p class="contact__line">
      <svg viewBox="0 0 16 16"><rect x="1" y="3" width="14" height="10" fill="var(--blue)"/><path d="M1 3l7 6 7-6" stroke="#fff" stroke-width="1.4" fill="none"/></svg>
      info@marbleshoredental.example
    </p>
    <p class="contact__line">
      <svg viewBox="0 0 16 16" fill="none" stroke="var(--blue)" stroke-width="1.4"><circle cx="8" cy="8" r="6.5"/><path d="M1.5 8h13M8 1.5c-3 3.5-3 9.5 0 13M8 1.5c3 3.5 3 9.5 0 13"/></svg>
      www.marbleshoredental.example
    </p>
  </div>
</section>

<section class="card card--back">
  <div class="appointment">
    <p class="appointment__field">Appointment Date</p>
    <p class="appointment__field">Time</p>
  </div>

  <div class="back-mark">Marble Shore<br>Dental</div>

  <div class="wave-band" role="img" aria-label="Decorative light blue wave band along the bottom of the card"></div>
  <p class="band-name">Marble Shore Dental</p>
</section>

</body>
</html>
```